Sudsy Harbor Laundromat Wordpress Design

We need a Wordpress website design for our laundromat, Sudsy Harbor Atlanta, at www.sudsyharborlaunder.example. We would like to have 6 pages: Home, About Us, Services, Locations, Reviews and Contact us. We will provide content for the text on each page. What we do: We are a full service laundromat that provides dry cleaning drop off, professional laundry services, wash dry fold and self service laundry to the local community. We would like to use the color scheme from our logo to convey a warm, safe, and bright business that caters to its diverse community.
Updates

I like the structure of this laundromat website: http://www.tumblewashexample.com/ Using my logo and color scheme in the above referenced website is what. Am looking for. The photos attached to the project with the female model should be used as a primary focus and supplemented by actual photos of the equipment.

Target Market(s)

Our target market is a diverse group of people from Midtown Atlanta - LGBTQ community /Locals/Regulars that have been coming to laundromat for 30 years.

Industry/Entity Type

Laundromat

Coding

Coded - Design and coding required

Number of Pages Required

5+ page

Font styles to use
Sans Serif

Colors
0054AA
0677BA
7BADD7
CADEEF
E8F1F8

Requirements
Must have
• Feature this video on the main page: https://videos.example.net/wq7PzrT2kLm

```html
<!DOCTYPE html>
<html lang="en">
<head>
<meta charset="utf-8">
<title>Sudsy Harbor Laundromat</title>
<link href="https://fonts.googleapis.com/css2?family=Kumbh+Sans:wght@400;500;600;700&display=swap" rel="stylesheet">
<style>
:root{
  --brand:#0054AA;
  --brand-mid:#0677BA;
  --brand-light:#7BADD7;
  --brand-pale:#CADEEF;
  --soft:#E8F1F8;
  --ink:#1c1c1c;
  --text:#4a4a4a;
  --muted:#8a8a8a;
  --line:#d3dde6;
  --night:#0d2440;
  --white:#ffffff;
}
*{margin:0;padding:0;box-sizing:border-box}
html,body{width:1200px;height:3924px;overflow:hidden;background:var(--white)}
body{font-family:"Kumbh Sans",sans-serif;color:var(--ink);position:relative}
.abs{position:absolute}
a{color:inherit;text-decoration:none}
/* header */
.site-header{left:0;top:0;width:1200px;height:94px;background:var(--white)}
.brand{left:195px;top:28px;font-size:30px;font-weight:700;color:var(--brand);display:flex;align-items:center;gap:10px}
.brand-dot{width:14px;height:14px;border-radius:50%;background:var(--brand)}
.main-nav a{position:absolute;top:36px;font-size:16px;font-weight:500;color:var(--ink);white-space:nowrap}
/* hero / featured video */
.hero{left:0;top:94px;width:1200px;height:606px;background:linear-gradient(90deg,#2f4256 0%,#7f94a8 30%,#b6c6d4 50%,#7f94a8 70%,#2c3f53 100%)}
.hero-curve{left:0;top:94px}
.hero-title{left:0;top:470px;width:1200px;text-align:center;color:var(--white);font-size:38px;font-weight:700;line-height:58px}
.play-btn{left:564px;top:330px;width:72px;height:72px;border-radius:50%;background:rgba(255,255,255,.9);display:flex;align-items:center;justify-content:center}
/* about */
.about-circle{border-radius:50%;background:var(--soft)}
.kicker{left:193px;top:824px;width:46px;height:3px;background:var(--brand)}
.about-title{left:193px;top:838px;font-size:28px;font-weight:500}
.about-text{left:193px;top:892px;width:380px;font-size:13.5px;line-height:24.4px;color:var(--text)}
.btn-outline{left:193px;top:1060px;width:154px;height:34px;border:2px solid var(--brand);border-radius:17px;font-size:13px;font-weight:600;display:flex;align-items:center;justify-content:center}
.badge{left:594px;top:987px;width:123px;height:46px;background:var(--brand);border-radius:4px;color:var(--white);display:flex;align-items:center;padding-left:12px;gap:6px}
.badge b{font-size:19px;font-weight:600}
.badge span{font-size:11px;line-height:13px}
/* services */
.services{left:0;top:1221px;width:1200px;height:1469px;background:var(--soft)}
.section-title{left:0;width:1200px;text-align:center;font-weight:600}
.section-sub{left:0;width:1200px;text-align:center;font-size:13px;color:var(--text)}
.service-title{font-size:26px;font-weight:500}
.service-rule{height:0;border-top:2px dotted #666}
.service-text{font-size:12px;line-height:24.4px;color:var(--text);width:372px}
/* testimonials */
.quote-card{background:var(--white);box-shadow:0 0 18px rgba(0,0,0,.05);padding:24px 30px 24px 54px;font-size:11.5px;line-height:21px;color:var(--text)}
.quote-mark{position:absolute;left:24px;color:var(--brand);font-size:34px;font-weight:700;line-height:1}
.author{display:flex;align-items:center;gap:16px}
.avatar{width:42px;height:42px;border-radius:50%;background:linear-gradient(#9fb4c8,#5b7390);border:2px solid var(--brand-pale)}
.author b{display:block;font-size:11px;font-weight:600;letter-spacing:.3px}
.author small{font-size:10.5px;color:var(--muted)}
.dot{width:8px;height:8px;border-radius:50%;border:1px solid #999;top:3060px}
/* contact */
.footer-bg{left:0;top:3420px;width:1200px;height:504px}
.contact-card{left:193px;top:3258px;width:812px;height:301px;background:var(--white);border-top:3px solid var(--brand);box-shadow:0 6px 20px rgba(0,0,0,.08)}
.contact-card h3{position:absolute;left:90px;top:26px;font-size:20px;font-weight:500}
.field{position:absolute;border:1px solid var(--line);border-radius:3px;font-size:10.5px;color:var(--muted);padding:8px 14px}
.submit{position:absolute;left:90px;top:239px;width:116px;height:30px;background:var(--brand);color:var(--white);font-size:12px;font-weight:700;display:flex;align-items:center;justify-content:center;border-radius:2px}
/* footer */
.footer-text{font-size:11.5px;line-height:18.4px;color:#d6e3ef}
.footer-head{font-size:12px;font-weight:700;color:var(--white);letter-spacing:.3px}
.footer-links{font-size:11.5px;line-height:19px;color:#d6e3ef}
.social{width:18px;height:18px;border-radius:50%;border:1.5px solid #d6e3ef;top:3739px}
.copy{font-size:11px;color:#d6e3ef}
</style>
</head>
<body>

<header class="abs site-header">
  <div class="abs brand"><span class="brand-dot"></span>Sudsy Harbor</div>
  <nav class="main-nav">
    <a style="left:528px">Home</a>
    <a style="left:592px">About Us</a>
    <a style="left:679px">Services</a>
    <a style="left:760px">Locations</a>
    <a style="left:850px">Reviews</a>
    <a style="left:929px">Contact us</a>
  </nav>
</header>

<section class="featured-video">
  <a href="https://videos.example.net/wq7PzrT2kLm" class="abs hero" role="img" aria-label="Featured video: a woman in a blue dress walking between rows of front-loading washers in the laundromat"></a>
  <svg class="abs hero-curve" width="1200" height="606" viewBox="0 0 1200 606">
    <path d="M0,553 Q600,659 1200,553 L1200,606 L0,606 Z" fill="#fff"/>
    <path d="M0,553 Q600,659 1200,553" fill="none" stroke="#0d2440" stroke-width="6"/>
  </svg>
  <a href="https://videos.example.net/wq7PzrT2kLm" class="abs play-btn" aria-label="Play video">
    <svg width="26" height="28" viewBox="0 0 26 28"><path d="M4,2 L24,14 L4,26 Z" fill="#0054AA"/></svg>
  </a>
  <h1 class="abs hero-title">Dry Cleaning &amp;<br>Professional Laundry</h1>
</section>

<section>
  <div class="abs about-circle" style="left:-183px;top:807px;width:274px;height:274px"></div>
  <div class="abs about-circle" style="left:716px;top:754px;width:384px;height:384px"></div>
  <div class="abs kicker"></div>
  <h2 class="abs about-title">About Us</h2>
  <p class="abs about-text">Midtown Atlanta's friendly full service laundromat for over 30 years. Drop off your dry cleaning, leave us your wash dry fold, or use our clean self service machines. A warm, safe and bright place where every neighbor is welcome, from first timers to our longtime regulars. Call us Today ! 208-555-0147</p>
  <div class="abs btn-outline">Book Service Now</div>
  <svg class="abs" style="left:665px;top:787px" width="360" height="360" viewBox="0 0 360 360" role="img" aria-label="Photo of a red-haired woman beside a washing machine">
    <defs><linearGradient id="gAbout" x1="0" x2="1"><stop offset="0" stop-color="#9fb0bf"/><stop offset=".5" stop-color="#c6ccd1"/><stop offset="1" stop-color="#a0623e"/></linearGradient></defs>
    <polygon points="180,12 340,96 340,264 180,348 20,264 20,96" fill="url(#gAbout)" stroke="#111" stroke-width="3" stroke-linejoin="round"/>
  </svg>
  <div class="abs badge"><b>30+</b><span>Years<br>Experience</span></div>
</section>

<section>
  <div class="abs services"></div>
  <h2 class="abs section-title" style="top:1276px;font-size:33px">Our Services</h2>
  <p class="abs section-sub" style="top:1327px">Dry cleaning, professional laundry, wash dry fold and self service laundry.</p>

  <svg class="abs" style="left:194px;top:1394px" width="340" height="340" viewBox="0 0 340 340" role="img" aria-label="Photo of a bright laundromat with rows of washers">
    <defs><linearGradient id="gS1" x1="0" y1="0" x2="0" y2="1"><stop offset="0" stop-color="#d9dcd9"/><stop offset="1" stop-color="#9ea3a2"/></linearGradient></defs>
    <polygon points="145,28 288,104 288,256 145,332 2,256 2,104" fill="none" stroke="#0677BA" stroke-width="3" stroke-linejoin="round"/>
    <polygon points="170,18 313,94 313,246 170,322 27,246 27,94" fill="url(#gS1)" stroke="#111" stroke-width="3" stroke-linejoin="round"/>
  </svg>
  <svg class="abs" style="left:520px;top:1405px" width="90" height="60" viewBox="0 0 90 60">
    <polygon points="24,26 38,34 38,50 24,58 10,50 10,34" fill="none" stroke="#0677BA" stroke-width="1.5"/>
    <polygon points="68,8 77,13 77,23 68,28 59,23 59,13" fill="#CADEEF"/>
  </svg>
  <h3 class="abs service-title" style="left:632px;top:1465px">Dry Clean Service</h3>
  <div class="abs service-rule" style="left:632px;top:1515px;width:311px"></div>
  <p class="abs service-text" style="left:632px;top:1538px">Drop off your garments on the way to work and pick them up crisp, pressed and ready to wear. Careful handling for suits, dresses and everyday clothes.</p>

  <svg class="abs" style="left:665px;top:1821px" width="340" height="340" viewBox="0 0 340 340" role="img" aria-label="Photo of a woman in a blue dress mopping in front of washers">
    <defs><linearGradient id="gS2" x1="0" y1="0" x2="0" y2="1"><stop offset="0" stop-color="#bcd7cf"/><stop offset=".55" stop-color="#a9aeac"/><stop offset="1" stop-color="#5e6d82"/></linearGradient></defs>
    <polygon points="195,28 338,104 338,256 195,332 52,256 52,104" fill="none" stroke="#0677BA" stroke-width="3" stroke-linejoin="round"/>
    <polygon points="170,18 313,94 313,246 170,322 27,246 27,94" fill="url(#gS2)" stroke="#111" stroke-width="3" stroke-linejoin="round"/>
  </svg>
  <svg class="abs" style="left:590px;top:1831px" width="90" height="60" viewBox="0 0 90 60">
    <polygon points="65,26 79,34 79,50 65,58 51,50 51,34" fill="none" stroke="#0677BA" stroke-width="1.5"/>
    <polygon points="21,8 30,13 30,23 21,28 12,23 12,13" fill="#CADEEF"/>
  </svg>
  <h3 class="abs service-title" style="left:256px;top:1892px">Leather &amp; Suede</h3>
  <div class="abs service-rule" style="left:256px;top:1942px;width:311px"></div>
  <p class="abs service-text" style="left:256px;top:1964px">Jackets, bags and shoes get specialist cleaning and conditioning, so leather and suede stay soft, rich in colour and ready for many more seasons.</p>

  <svg class="abs" style="left:194px;top:2247px" width="340" height="340" viewBox="0 0 340 340" role="img" aria-label="Photo of three stacked front-loading washers">
    <defs><linearGradient id="gS3" x1="0" y1="0" x2="0" y2="1"><stop offset="0" stop-color="#b7cabf"/><stop offset=".5" stop-color="#8f9594"/><stop offset="1" stop-color="#c8c8c4"/></linearGradient></defs>
    <polygon points="145,28 288,104 288,256 145,332 2,256 2,104" fill="none" stroke="#0677BA" stroke-width="3" stroke-linejoin="round"/>
    <polygon points="170,18 313,94 313,246 170,322 27,246 27,94" fill="url(#gS3)" stroke="#111" stroke-width="3" stroke-linejoin="round"/>
  </svg>
  <svg class="abs" style="left:520px;top:2256px" width="90" height="60" viewBox="0 0 90 60">
    <polygon points="24,26 38,34 38,50 24,58 10,50 10,34" fill="none" stroke="#0677BA" stroke-width="1.5"/>
    <polygon points="68,8 77,13 77,23 68,28 59,23 59,13" fill="#CADEEF"/>
  </svg>
  <h3 class="abs service-title" style="left:632px;top:2317px">Wash Dry Fold</h3>
  <div class="abs service-rule" style="left:632px;top:2366px;width:311px"></div>
  <p class="abs service-text" style="left:632px;top:2390px">Leave your laundry with us and we wash, dry and neatly fold it the same day. Priced by the pound, with fresh scents and gentle care.</p>
</section>

<section>
  <div class="abs quote-card" style="left:218px;top:2836px;width:365px;height:119px"><span class="quote-mark" style="top:30px">&ldquo;</span>Lorem ipsum dolor sit amet, consectetur adipiscing elit. Nullam ac tellus urna. Phasellus dictum et purus iaculis accumsan. Sed suscipit pharetra.</div>
  <div class="abs quote-card" style="left:620px;top:2769px;width:362px;height:186px"><span class="quote-mark" style="top:30px">&ldquo;</span>Lorem ipsum dolor sit amet, consectetur adipiscing elit. Nullam ac tellus urna. Phasellus dictum et purus iaculis accumsan. Sed suscipit pharetra dolor in venenatis. Vivamus eget finibus ipsum, quis placerat sem. Nulla varius erat in libero ornare dignissim. Nam a interdum.</div>
  <div class="abs author" style="left:236px;top:2982px"><span class="avatar"></span><div><b>MARLA DENNING, FOUNDER</b><small>Westfield Advisory Group</small></div></div>
  <div class="abs author" style="left:638px;top:2982px"><span class="avatar" style="background:linear-gradient(#7BADD7,#0054AA)"></span><div><b>THEO VARGA, CO-FOUNDER</b><small>Brightline Studio</small></div></div>
  <span class="abs dot" style="left:584px;background:var(--brand);border-color:var(--brand)"></span>
  <span class="abs dot" style="left:596px"></span>
  <span class="abs dot" style="left:608px"></span>
</section>

<section>
  <h2 class="abs section-title" style="top:3150px;font-size:34px;font-weight:700">CONTACT</h2>
  <p class="abs section-sub" style="top:3193px;font-size:14px;line-height:20px;color:var(--ink)">Lorem ipsum dolor sit amet, consectetur adipiscing elit<br>Nunc ac consectetur leo. Mauris aliquam.</p>
  <svg class="abs footer-bg" width="1200" height="504" viewBox="0 0 1200 504">
    <defs><linearGradient id="gNight" x1="0" y1="0" x2="0" y2="1"><stop offset="0" stop-color="#123057"/><stop offset="1" stop-color="#0a1c33"/></linearGradient></defs>
    <path d="M0,22 Q300,40 600,28 Q900,14 1200,34 L1200,504 L0,504 Z" fill="url(#gNight)"/>
  </svg>
  <div class="abs contact-card">
    <h3>Feel Free to Contact Us</h3>
    <div class="field" style="left:90px;top:64px;width:311px;height:29px">First Name</div>
    <div class="field" style="left:413px;top:64px;width:311px;height:29px">Last Name</div>
    <div class="field" style="left:90px;top:108px;width:311px;height:29px">Email</div>
    <div class="field" style="left:413px;top:108px;width:311px;height:29px">Subject</div>
    <div class="field" style="left:90px;top:151px;width:634px;height:73px">Message...</div>
    <div class="submit">SUBMIT</div>
  </div>
</section>

<footer>
  <p class="abs footer-text" style="left:209px;top:3640px;width:290px">Lorem ipsum dolor sit amet, consectetur adipiscing elit. Aenean massa mauris, maximus nec faucibus a, malesuada ut magna. Lorem ipsum dolor sit amet, consectetur adipiscing elit. Aenean massa mauris, maximus nec faucibus a, malesuada ut magna.</p>
  <div class="abs footer-head" style="left:576px;top:3638px">SITELINKS</div>
  <div class="abs" style="left:576px;top:3660px;width:160px;border-top:1px solid #2b4a70"></div>
  <div class="abs footer-links" style="left:576px;top:3669px">Home<br>About Us<br>Services<br>Locations<br>Reviews<br>Contact</div>
  <div class="abs footer-head" style="left:827px;top:3638px">STAY IN TOUCH</div>
  <div class="abs" style="left:827px;top:3660px;width:178px;border-top:1px solid #2b4a70"></div>
  <div class="abs footer-links" style="left:827px;top:3670px">Subscribe Our Newsletter</div>
  <div class="abs" style="left:827px;top:3698px;width:108px;height:24px;background:var(--white)"></div>
  <div class="abs" style="left:935px;top:3698px;width:70px;height:24px;background:var(--brand-mid);color:var(--white);font-size:11px;display:flex;align-items:center;justify-content:center">Subscribe</div>
  <span class="abs social" style="left:829px"></span>
  <span class="abs social" style="left:853px"></span>
  <span class="abs social" style="left:877px"></span>
  <div class="abs" style="left:181px;top:3815px;width:838px;border-top:1px solid #2b4a70"></div>
  <div class="abs copy" style="left:181px;top:3837px">@ 2021 Sudsyharboratlanta. All Rights Reserved.</div>
  <div class="abs copy" style="left:849px;top:3837px">Privace &amp; Policy &nbsp;|&nbsp; Faq &nbsp;|&nbsp; Terms.</div>
</footer>

</body>
</html>
```